Pelton Mortgage Capital Business Card

We need a business card design for our mortgage servicing company. In addition to servicing the loans of homeowners, we help homeowners with purchasing their homes and any mortgage refinancing. We would like to see designs that use the colors in the logo attached below (gold-ish yellow and navy blue), and any other design you deem fit! The design should communicate a simpler life with smart mortgages provided by Pelton.

```html
<!DOCTYPE html>
<html lang="en">
<head>
<meta charset="UTF-8">
<title>Pelton Mortgage Capital Business Card</title>
<link rel="stylesheet" href="https://fonts.googleapis.com/css2?family=Playfair+Display:wght@700&family=Poppins:wght@400;500;600&display=swap">
<style>
  :root {
    --navy: #1f1d4d;
    --gold: #d4a22c;
    --gold-soft: #f7dfa0;
    --pink-soft: #f3c6d8;
    --ink: #1b1b1f;
    --card: #ffffff;
    --backdrop: #ecebea;
    --rule: #b9b9bd;
  }
  * { box-sizing: border-box; margin: 0; padding: 0; }
  html, body { width: 1200px; height: 880px; overflow: hidden; }
  body {
    background: var(--backdrop);
    font-family: "Poppins", sans-serif;
    position: relative;
  }
  .card {
    position: absolute;
    left: 300px;
    width: 600px;
    height: 343px;
    background: var(--card);
    border-radius: 18px;
    overflow: hidden;
    box-shadow: 0 10px 30px rgba(0,0,0,0.18);
  }
  .card--front { top: 50px; }
  .card--back { top: 480px; }

  .wash { position: absolute; }
  .wash--gold {
    background: radial-gradient(ellipse at center, var(--gold-soft) 0%, rgba(247,223,160,0.55) 55%, rgba(247,223,160,0) 75%);
  }
  .wash--pink {
    background: radial-gradient(ellipse at center, var(--pink-soft) 0%, rgba(243,198,216,0.55) 55%, rgba(243,198,216,0) 75%);
  }
  .card--front .wash--gold { left: 160px; top: -140px; width: 520px; height: 300px; }
  .card--front .wash--pink { left: -120px; top: 170px; width: 620px; height: 300px; }
  .card--back .wash--gold { left: -120px; top: -60px; width: 480px; height: 330px; }
  .card--back .wash--pink { left: 300px; top: 40px; width: 420px; height: 340px; }

  .brand {
    position: absolute;
    display: flex;
    align-items: center;
    gap: 12px;
    color: var(--navy);
    font-weight: 600;
    white-space: nowrap;
  }
  .brand__dot {
    width: 18px; height: 18px;
    border-radius: 50%;
    background: var(--gold);
  }
  .card--front .brand { left: 0; right: 0; justify-content: center; top: 118px; font-size: 50px; }
  .card--back .brand { left: 60px; top: 60px; font-size: 38px; }

  .front-url {
    position: absolute;
    left: 0; right: 0;
    top: 238px;
    text-align: center;
    font-size: 14px;
    letter-spacing: 4px;
    color: var(--ink);
  }

  .divider {
    position: absolute;
    height: 1px;
    background: var(--rule);
  }
  .divider--main { left: 270px; right: 40px; top: 170px; }
  .divider--name { left: 50px; width: 200px; top: 250px; }

  .address {
    position: absolute;
    right: 40px;
    top: 182px;
    text-align: right;
    font-size: 13px;
    line-height: 1.45;
    color: var(--ink);
  }
  .person { position: absolute; left: 50px; top: 180px; }
  .person__name {
    font-family: "Playfair Display", serif;
    font-size: 28px;
    color: var(--ink);
    line-height: 1.1;
  }
  .person__role { font-size: 14px; color: var(--gold); margin-top: 2px; }

  .contacts {
    position: absolute;
    left: 50px;
    top: 262px;
    list-style: none;
    font-size: 13.5px;
    color: var(--ink);
  }
  .contacts li { display: flex; align-items: center; gap: 10px; line-height: 22px; }
  .contacts svg { width: 13px; height: 13px; fill: var(--gold); flex: none; }
</style>
</head>
<body>

<section class="card card--front">
  <div class="wash wash--gold" role="img" aria-label="Soft gold watercolour wash"></div>
  <div class="wash wash--pink" role="img" aria-label="Soft pink watercolour wash"></div>
  <div class="brand"><span class="brand__dot"></span>Pelton Mortgage</div>
  <p class="front-url">WWW.PELTONMORTGAGE.COM</p>
</section>

<section class="card card--back">
  <div class="wash wash--gold" role="img" aria-label="Soft gold watercolour wash"></div>
  <div class="wash wash--pink" role="img" aria-label="Soft pink watercolour wash"></div>
  <div class="brand"><span class="brand__dot"></span>Pelton Mortgage</div>

  <div class="divider divider--main"></div>
  <p class="address">P.O. Box 417 2290 Harbor Rd<br>Linden Nebraska 20744</p>

  <div class="person">
    <h1 class="person__name">Evan Carter</h1>
    <p class="person__role">Managing Director</p>
  </div>
  <div class="divider divider--name"></div>

  <ul class="contacts">
    <li>
      <svg viewBox="0 0 24 24" aria-hidden="true"><path d="M6.6 10.8a15.1 15.1 0 0 0 6.6 6.6l2.2-2.2a1 1 0 0 1 1-.25 11.4 11.4 0 0 0 3.6.57 1 1 0 0 1 1 1V20a1 1 0 0 1-1 1A17 17 0 0 1 3 4a1 1 0 0 1 1-1h3.5a1 1 0 0 1 1 1c0 1.25.2 2.45.57 3.6a1 1 0 0 1-.25 1z"/></svg>
      (555) 014-2286
    </li>
    <li>
      <svg viewBox="0 0 24 24" aria-hidden="true"><path d="M2 5h20v14H2z M2 5l10 8 10-8" /></svg>
      evan.carter@peltonmortgage.com
    </li>
    <li>
      <svg viewBox="0 0 24 24" aria-hidden="true"><circle cx="12" cy="12" r="10"/></svg>
      www.peltonmortgage.com
    </li>
  </ul>
</section>

</body>
</html>
```